redesing professional certificate

Redesign our certificate to more a professional look and to make it look like a-wanna have - Best in adobe photoshop, because this template will be our basic, and we have in our education different levels, basic, upper, lower, complex, master level. I usually add a small picture to show what level they are. Or when you have a better suggestion I a gladly to hear.
We teach to physiotherapist so it has to look professional.

Target Market(s)

physiotherapist

Industry/Entity Type

Health Care

Requirements
Must have
• our logo

```html
<!DOCTYPE html>
<html lang="en">
<head>
<meta charset="utf-8">
<title>Certificate of Training</title>
<link rel="stylesheet" href="https://fonts.googleapis.com/css2?family=Arimo:ital,wght@0,400;1,400&family=Playfair+Display:wght@700&display=swap">
<style>
  :root {
    --backdrop: #b6d4e1;
    --paper: #ffffff;
    --navy: #1b2340;
    --navy-deep: #14304a;
    --orange: #f7a70f;
    --ink: #1e1e24;
  }
  * { margin: 0; padding: 0; box-sizing: border-box; }
  html, body { width: 900px; height: 1200px; overflow: hidden; }
  body { background: var(--backdrop); position: relative; font-family: "Arimo", Arial, sans-serif; color: var(--ink); }
  .certificate { position: absolute; left: 114px; top: 102px; width: 685px; height: 969px; background: var(--paper); }
  .side-panel { position: absolute; left: 0; top: 0; width: 167px; height: 969px; }
  .abs { position: absolute; white-space: nowrap; }
  .title { left: 204px; top: 66px; font-family: "Playfair Display", Georgia, serif; font-weight: 700; font-size: 54px; line-height: 63px; color: var(--orange); }
  .intro { left: 212px; top: 233px; font-size: 17px; }
  .recipient { left: 212px; top: 261px; font-size: 28px; color: var(--navy); }
  .course { left: 215px; top: 303px; font-size: 17px; line-height: 22px; color: var(--navy); }
  .course .course-name { font-size: 20px; }
  .signature { position: absolute; top: 491px; width: 161px; border-top: 1.5px solid var(--navy); padding-top: 6px; }
  .signature.left { left: 218px; }
  .signature.right { left: 480px; text-align: right; padding-top: 2px; }
  .signer { font-size: 18px; color: var(--navy); line-height: 21px; }
  .role { font-size: 14px; font-style: italic; color: var(--navy); line-height: 17px; }
  .registration { left: 217px; top: 573px; font-size: 16px; }
  .terms { left: 217px; top: 617px; font-size: 16px; line-height: 20px; white-space: normal; width: 422px; }
  .brand-mark { position: absolute; left: 200px; top: 750px; width: 104px; height: 104px; display: flex; flex-direction: column; align-items: center; justify-content: center; gap: 6px; }
  .brand-dot { width: 44px; height: 44px; border-radius: 50%; background: var(--navy); }
  .brand-name { font-size: 16px; color: var(--navy); }
  .company { left: 339px; top: 753px; color: var(--ink); }
  .company-name { font-size: 22px; line-height: 26px; }
  .company-address { font-size: 16px; line-height: 20px; }
  .tagline { position: absolute; left: 336px; top: 823px; width: 302px; height: 24px; background: var(--navy-deep); color: #fff; font-size: 16px; line-height: 24px; text-align: center; }
</style>
</head>
<body>
  <main class="certificate">
    <svg class="side-panel" viewBox="0 0 167 969" role="img" aria-label="Flowing fine-line wave pattern on navy band">
      <defs>
        <linearGradient id="panelWave" x1="0" y1="0" x2="1" y2="1">
          <stop offset="0" stop-color="#1b2340"/>
          <stop offset="0.5" stop-color="#2a3357"/>
          <stop offset="1" stop-color="#1b2340"/>
        </linearGradient>
      </defs>
      <rect width="167" height="969" fill="url(#panelWave)"/>
    </svg>

    <h1 class="abs title">Certificate of<br>Training</h1>
    <p class="abs intro">This is to certify that</p>
    <p class="abs recipient">Lena Marsh</p>
    <p class="abs course">has completed the course <span class="course-name">Fasciatherapy level I</span><br>undertaken on 15th-17th February 2020<br>at Kopavogur, Iceland</p>

    <div class="signature left">
      <p class="signer">Mr JT van Dalen</p>
      <p class="role">Co-Director</p>
    </div>
    <div class="signature right">
      <p class="signer">Mr RS Okafor</p>
      <p class="role">Co-Director</p>
    </div>

    <p class="abs registration">Registration number: 7 ICE 20</p>
    <p class="abs terms">The Myoline Tissue Method ongoing certification is contingent upon meeting the requirements of maintenance of the certification of Fasciatherapy.</p>

    <div class="brand-mark">
      <span class="brand-dot"></span>
      <span class="brand-name">Myoline</span>
    </div>
    <div class="abs company">
      <p class="company-name">Myoline BV</p>
      <p class="company-address">Lindenkade 14</p>
      <p class="company-address">4811KX Westerhaven, The Netherlands</p>
    </div>
    <p class="tagline">Specialists in Fasciatherapy Innovation</p>
  </main>
</body>
</html>
```